velto fulfilment website design wordpress

I'm looking for a website design (WordPress) for an order fulfillment company. the company is a micro-fulfillment company that offers the following services: inventory management, order fulfillment, returns, and storage. the site must have a multilanguage feature.

the website must look modern and professional. Also, the website should not look like it came from a template.

sample site:
https://go-pakmo.nl/fulfilment-tarieven/
https://www.zendrix.com/

Target Market(s)

ecommerce owner

Industry/Entity Type

logistics

Coding

Coded - Design and coding required

Number of Pages Required

5+ page

Colors
0054AA
0677BA
7BADD7
CADEEF
E8F1F8

Requirements
Must have
• multilanguage
Should not have
• look that the design came from a template

```html
<!DOCTYPE html>
<html lang="en">
<head>
<meta charset="utf-8">
<title>Velto Fulfilment</title>
<link href="https://fonts.googleapis.com/css2?family=IBM+Plex+Sans:ital,wght@0,500;0,600;0,700;1,600&family=Roboto:wght@400;500;700&display=swap" rel="stylesheet">
<style>
:root{
  --navy:#2f5479;
  --blue:#3d6690;
  --sky:#6aaee8;
  --sky-soft:#7badd7;
  --ink:#333a42;
  --mist:#f2f3f5;
  --white:#ffffff;
}
*{box-sizing:border-box;margin:0;padding:0}
html,body{width:1200px;height:3821px;overflow:hidden}
body{font-family:'Roboto',sans-serif;color:var(--ink);background:var(--white);position:relative}
section,header,footer,.topbar{position:absolute;left:0;width:1200px}
.abs{position:absolute}
h2.title{font-family:'IBM Plex Sans',sans-serif;font-weight:700;font-size:37px;color:var(--blue);letter-spacing:.5px;text-align:center;position:absolute;left:0;width:1200px}
h2.title::after{content:"";display:block;width:62px;height:3px;background:var(--sky);margin:4px auto 0}
.btn{position:absolute;background:var(--sky);color:var(--white);font-family:'Roboto',sans-serif;font-weight:700;font-size:15px;display:flex;align-items:center;justify-content:center;letter-spacing:.2px}

.topbar{top:0;height:41px;background:linear-gradient(90deg,#1f3f60 0%,#27496e 62%,#5d7ea3 100%);color:var(--white);font-size:13px}
.topbar .slant{position:absolute;left:740px;top:0;width:460px;height:41px;background:linear-gradient(90deg,#4c6f96,#7592b4);clip-path:polygon(30px 0,100% 0,100% 100%,0 100%)}
.topbar .contact{position:absolute;left:111px;top:12px;display:flex;gap:14px;align-items:center}
.topbar .right{position:absolute;right:111px;top:12px;display:flex;gap:16px;align-items:center;font-weight:700;font-size:12px}
.topbar .dot{width:10px;height:10px;border-radius:50%;background:var(--white)}

header{top:41px;height:113px;background:var(--white)}
.brand{position:absolute;left:111px;top:40px;display:flex;align-items:center;gap:12px;font-family:'IBM Plex Sans',sans-serif;font-weight:700;font-size:24px;color:var(--navy);letter-spacing:.3px}
.brand .mark{width:22px;height:22px;background:var(--navy)}
.nav{position:absolute;left:411px;top:47px;display:flex;gap:25px;font-family:'IBM Plex Sans',sans-serif;font-style:italic;font-weight:600;font-size:15px;color:var(--navy)}
.nav .on{color:var(--sky)}

.hero{top:154px;height:659px;overflow:hidden}
.hero .photo{position:absolute;inset:0;background:linear-gradient(100deg,#efe7de 0%,#e9ddcc 35%,#d9b48a 55%,#e8e2dc 75%,#f3f1ee 100%)}
.hero svg{position:absolute;left:0;top:0}
.hero .welcome{position:absolute;left:111px;top:154px;font-family:'IBM Plex Sans',sans-serif;font-weight:500;font-size:21px;color:var(--blue)}
.hero h1{position:absolute;left:111px;top:182px;font-family:'IBM Plex Sans',sans-serif;font-weight:700;font-size:39px;color:var(--blue);letter-spacing:.5px}
.hero p{position:absolute;left:111px;top:240px;width:450px;font-size:18px;line-height:29px;color:#222}

.about{top:813px;height:433px}
.about .title{top:-18px}
.about .copy{position:absolute;left:130px;width:940px;top:52px;text-align:center;font-size:15.5px;line-height:28px;color:#444}
.about .copy p+p{margin-top:13px}

.services{top:1246px;height:736px;background:linear-gradient(120deg,#2d5075 0%,#3e6590 45%,#46709a 70%,#3a618a 100%);overflow:hidden}
.services .title{top:50px;color:var(--white)}
.services .title::after{background:var(--white)}
.services svg{position:absolute;left:0;top:0}
.services .label{position:absolute;left:790px;font-family:'Roboto',sans-serif;font-weight:700;font-size:19px;color:var(--white);letter-spacing:.2px}
.services .core{position:absolute;left:240px;top:1633px}
.core-name{position:absolute;left:363px;top:406px;transform:translate(-50%,-50%);font-family:'IBM Plex Sans',sans-serif;font-weight:700;font-size:22px;color:var(--navy);white-space:nowrap;display:flex;align-items:center;gap:10px}
.core-name .mark{width:16px;height:16px;background:var(--navy)}

.why{top:1982px;height:655px}
.why h2{position:absolute;left:111px;top:140px;font-family:'IBM Plex Sans',sans-serif;font-weight:700;font-size:37px;color:var(--blue)}
.why h2::after{content:"";display:block;width:62px;height:3px;background:var(--sky);margin-top:6px}
.why .copy{position:absolute;left:113px;top:226px;width:436px;font-size:15.5px;line-height:28.5px;color:#444;text-align:justify}
.why .copy p+p{margin-top:10px}
.why .frame{position:absolute;left:635px;top:151px;width:452px;height:391px;border:4px solid var(--sky)}
.why .photo{position:absolute;left:599px;top:115px;width:455px;height:394px;background:linear-gradient(110deg,#6b5a45 0%,#a8894f 30%,#c9c2ad 50%,#4a5566 75%,#2b2f36 100%)}

.trusted{top:2637px;height:312px;background:var(--mist)}
.trusted .title{top:62px}
.logos{position:absolute;left:111px;top:153px;display:flex;gap:22px}
.logos .card{width:178px;height:86px;background:var(--white);box-shadow:0 2px 8px rgba(0,0,0,.08);display:flex;align-items:center;justify-content:center;font-family:'IBM Plex Sans',sans-serif;font-weight:600;font-size:16px;color:#222}
.trusted .arrow{position:absolute;top:188px;width:34px;height:34px;border-radius:50%;display:flex;align-items:center;justify-content:center}
.arrow.prev{left:33px;background:var(--white);border:2px solid var(--sky-soft)}
.arrow.next{left:1131px;background:var(--sky)}

.contact{top:2949px;height:498px}
.contact .title{top:86px}
.field{position:absolute;background:var(--white);box-shadow:0 2px 10px rgba(0,0,0,.1);font-size:15px;color:#333;padding:14px 17px}
.contact .btn{left:518px;top:347px;width:163px;height:49px;font-size:14px}

footer{top:3447px;height:374px;background:var(--blue);color:var(--white)}
footer .brand{left:111px;top:155px;color:var(--white);font-size:24px}
footer .brand .mark{background:var(--white)}
footer .col{position:absolute;top:60px}
footer h4{font-family:'Roboto',sans-serif;font-weight:700;font-size:17px;margin-bottom:20px}
footer ul{list-style:none;font-size:15px}
footer li{height:41px;display:flex;align-items:flex-start;gap:19px}
footer li::before{content:"";width:5px;height:5px;border-radius:50%;background:var(--sky);margin-top:7px}
footer .info{font-size:15px;line-height:22px}
footer .info div{display:flex;gap:14px;margin-bottom:17px}
footer .info svg{flex:none;margin-top:3px}
footer .rule{position:absolute;left:111px;top:305px;width:978px;height:1px;background:rgba(255,255,255,.35)}
footer .copy{position:absolute;left:432px;top:326px;font-size:14px}
footer .social{position:absolute;left:969px;top:318px;display:flex;gap:8px}
footer .social span{width:34px;height:34px;border-radius:50%;background:var(--sky)}
</style>
</head>
<body>

<div class="topbar">
  <div class="slant"></div>
  <div class="contact">
    <svg width="12" height="12" viewBox="0 0 24 24"><path fill="#7badd7" d="M6.6 10.8a15 15 0 0 0 6.6 6.6l2.2-2.2c.3-.3.7-.4 1-.2 1.1.4 2.3.6 3.6.6.6 0 1 .4 1 1V20c0 .6-.4 1-1 1A17 17 0 0 1 3 4c0-.6.4-1 1-1h3.5c.6 0 1 .4 1 1 0 1.3.2 2.5.6 3.6.1.3 0 .7-.2 1z"/></svg>
    <span>+1 (555) 010 2040</span><span>|</span>
    <svg width="14" height="12" viewBox="0 0 24 20"><path fill="#7badd7" d="M2 0h20a2 2 0 0 1 2 2v1l-12 7L0 3V2a2 2 0 0 1 2-2zm-2 6l12 7 12-7v12a2 2 0 0 1-2 2H2a2 2 0 0 1-2-2z"/></svg>
    <span>info@veltofulfilment.com</span>
  </div>
  <div class="right">
    <span class="dot"></span><span class="dot"></span><span class="dot"></span>
    <span>|</span><span>ENG ⌄</span>
  </div>
</div>

<header>
  <div class="brand"><span class="mark"></span>VELTO FULFILMENT</div>
  <nav class="nav">
    <span class="on">HOME</span><span>ABOUT US</span><span>OUR SERVICES</span><span>RESOURCES</span><span>CONTACT US</span>
  </nav>
  <div class="btn" style="left:951px;top:32px;width:138px;height:49px;font-size:14px">GET A QUOTE</div>
</header>

<section class="hero">
  <div class="photo" role="img" aria-label="Photo of a woman packing an order at a desk beside a laptop and parcel boxes"></div>
  <svg width="1200" height="659" viewBox="0 0 1200 659">
    <polygon points="0,634 600,480 1200,652 1200,659 0,659" fill="#3d6690"/>
    <polygon points="0,659 600,506 1200,659" fill="#ffffff"/>
  </svg>
  <div class="welcome">WELCOME TO</div>
  <h1>VELTO FULFILMENT</h1>
  <p>Lorem ipsum dolor sit amet, consectetur adipiscing elit, sed do eiusmod tempor incidea.</p>
  <div class="btn" style="left:111px;top:322px;width:137px;height:48px;font-size:14px">GET STARTED</div>
</section>

<section class="about">
  <h2 class="title">ABOUT US</h2>
  <div class="copy">
    <p>Lorem ipsum dolor sit amet, consectetur adipiscing elit, sed do eiusmod tempor incididunt ut labore et dolore magna aliqua. Ut enim ad minim veniam, quis nostrud exercitation ullamco laboris nisi ut aliquip ex ea commodo consequat. Duis aute irure dolor in reprehenderit in voluptate velit esse cillum dolore eu fugiat nulla pariatur. Excepteur sint occaecat cupidatat non proident, sunt in culpa qui officia deseullamco laboris nisi ut commodo runt mollit anim id est laborum.</p>
    <p>Lorem ipsum dolor sit amet, consectetur adipiscing elit, sed do eiusmod tempor incididunt ut labore et dolore magna aliqua. Ut enim ad minim veniam, quis nostrud exercitation ullamco laboris nisi ut aliquip ex ea commodo consequat. Duis aute irure dolor in reprehenderit in voluptate velit esse cillum dolore eu fugiat nulla pariatur.</p>
  </div>
  <div class="btn" style="left:525px;top:296px;width:150px;height:50px">LEARN MORE</div>
</section>

<section class="services" role="img" aria-label="Services diagram over a softly tinted office background">
  <h2 class="title">OUR SERVICES</h2>
  <svg width="1200" height="736" viewBox="0 0 1200 736">
    <g fill="none" stroke="#ffffff" stroke-width="2">
      <polyline points="650,190 549,190 470,267"/>
      <line x1="650" y1="335" x2="534" y2="335"/>
      <line x1="650" y1="479" x2="534" y2="479"/>
      <polyline points="650,623 549,623 470,545"/>
      <polyline points="412,207 608,405 412,605" stroke-dasharray="5 5"/>
    </g>
    <g fill="#ffffff">
      <polygon points="363,218 551,406 363,594 175,406"/>
      <polygon points="697,140 747,190 697,240 647,190"/>
      <polygon points="697,429 747,479 697,529 647,479"/>
      <polygon points="697,573 747,623 697,673 647,623"/>
    </g>
    <polygon points="697,285 747,335 697,385 647,335" fill="#6aaee8"/>
    <g fill="#6aaee8" stroke="#ffffff" stroke-width="2">
      <circle cx="470" cy="267" r="7"/><circle cx="534" cy="335" r="7"/>
      <circle cx="534" cy="479" r="7"/><circle cx="470" cy="545" r="7"/>
    </g>
    <g fill="none" stroke="#6aaee8" stroke-width="2">
      <rect x="684" y="178" width="14" height="12"/><rect x="698" y="178" width="12" height="12"/><rect x="690" y="168" width="12" height="10"/>
      <rect x="685" y="466" width="22" height="18" transform="rotate(-15 696 475)"/><path d="M684 494a10 10 0 0 1 10-8"/>
      <path d="M682 634v-16l15-10 15 10v16z"/><rect x="690" y="622" width="14" height="12"/>
    </g>
    <g fill="none" stroke="#ffffff" stroke-width="2">
      <circle cx="697" cy="335" r="17"/><rect x="689" y="328" width="16" height="14"/><line x1="689" y1="333" x2="705" y2="333"/>
    </g>
  </svg>
  <div class="core-name"><span class="mark"></span>VELTO FULFILMENT</div>
  <div class="label" style="top:178px">INVENTORY MANAGEMENT</div>
  <div class="label" style="top:322px">ORDER FULFILLMENT</div>
  <div class="label" style="top:466px">RETURNS</div>
  <div class="label" style="top:610px">STORAGE</div>
</section>

<section class="why">
  <h2>WHY WORK WITH US</h2>
  <div class="copy">
    <p>Lorem ipsum dolor sit amet, consectetur adipiscing elit, sed do eiusmod tempor incididunt ut labore et dolore magna aliqua. Ut enim ad minim veniam, quis nostrud exercitation ullamco laboris nisi utea.</p>
    <p>Lorem ipsum dolor sit amet, consectetur adipiscing elit, sed do eiusmod tempor incididunt ut labore et dolore magna aliqua utenim ad minimea.</p>
  </div>
  <div class="btn" style="left:113px;top:462px;width:149px;height:49px">LEARN MORE</div>
  <div class="frame"></div>
  <div class="photo" role="img" aria-label="Photo of a warehouse worker in a safety vest using a computer with inventory data"></div>
</section>

<section class="trusted">
  <h2 class="title">TRUSTED BY</h2>
  <div class="arrow prev"><svg width="10" height="12" viewBox="0 0 10 12"><path d="M7 1 2 6l5 5" fill="none" stroke="#3d6690" stroke-width="2"/></svg></div>
  <div class="logos">
    <div class="card">Nordvane</div>
    <div class="card">Brantwell</div>
    <div class="card">Parcelio</div>
    <div class="card">Stackora</div>
    <div class="card">Quillro</div>
  </div>
  <div class="arrow next"><svg width="10" height="12" viewBox="0 0 10 12"><path d="M3 1l5 5-5 5" fill="none" stroke="#fff" stroke-width="2"/></svg></div>
</section>

<section class="contact">
  <h2 class="title">CONTACT US</h2>
  <div class="field" style="left:165px;top:177px;width:283px;height:48px">Full Name</div>
  <div class="field" style="left:458px;top:177px;width:283px;height:48px">Phone</div>
  <div class="field" style="left:750px;top:177px;width:284px;height:48px">Email Address</div>
  <div class="field" style="left:165px;top:237px;width:869px;height:92px">Message</div>
  <div class="btn">SEND MESSAGE</div>
</section>

<footer>
  <div class="brand"><span class="mark"></span>VELTO FULFILMENT</div>
  <div class="col" style="left:423px">
    <h4>NAVIGATION</h4>
    <ul><li>Home</li><li>About Us</li><li>Our Services</li><li>Resources</li><li>Contact Us</li></ul>
  </div>
  <div class="col" style="left:600px">
    <h4>QUICK LINKS</h4>
    <ul><li>Privacy Policy</li><li>Terms &amp; Conditions</li><li>Legal Support</li><li>Disclaimer</li></ul>
  </div>
  <div class="col info" style="left:841px;width:250px">
    <h4>CONTACT US</h4>
    <div><svg width="12" height="15" viewBox="0 0 12 16"><path fill="#6aaee8" d="M6 0a6 6 0 0 1 6 6c0 4-6 10-6 10S0 10 0 6a6 6 0 0 1 6-6zm0 4a2 2 0 1 0 0 4 2 2 0 0 0 0-4z"/></svg><span>465, Lorum Ipsum Dolore Sed,<br>United States</span></div>
    <div><svg width="13" height="13" viewBox="0 0 24 24"><path fill="#6aaee8" d="M6.6 10.8a15 15 0 0 0 6.6 6.6l2.2-2.2c.3-.3.7-.4 1-.2 1.1.4 2.3.6 3.6.6.6 0 1 .4 1 1V20c0 .6-.4 1-1 1A17 17 0 0 1 3 4c0-.6.4-1 1-1h3.5c.6 0 1 .4 1 1 0 1.3.2 2.5.6 3.6.1.3 0 .7-.2 1z"/></svg><span>+1 (555) 010 2040</span></div>
    <div><svg width="15" height="12" viewBox="0 0 24 20"><path fill="#6aaee8" d="M2 0h20a2 2 0 0 1 2 2v1l-12 7L0 3V2a2 2 0 0 1 2-2zm-2 6l12 7 12-7v12a2 2 0 0 1-2 2H2a2 2 0 0 1-2-2z"/></svg><span>info@veltofulfilment.com</span></div>
  </div>
  <div class="rule"></div>
  <div class="copy">© 2023 VELTO FULFILMENT &nbsp;|&nbsp; All Rights Reserved</div>
  <div class="social"><span></span><span></span><span></span></div>
</footer>

</body>
</html>
```